Webdesign für Projektmanagement
Zielgruppe
Projektmanagement und Projektsteuerung von Bauvorhaben für Projektentwickler und Bauträger.
Wesentliche Bereiche sind Wirtschaftliche Steuerung, Steuerung der Baustelle und Bauabläufe sowie Steuerung der Marketing und Vertriebsaktivitäten.
Aufgabenstellung
Orientierung am Logo. Logo und Visitenkarte liegen bei. Schriftart Prelo und Prelo Slab.

```html
<!DOCTYPE html>
<html lang="de">
<head>
<meta charset="utf-8">
<title>Brandvik Real Estate – Projektmanagement</title>
<link href="https://fonts.googleapis.com/css2?family=Roboto+Slab:wght@400;700&family=Roboto:wght@400&display=swap" rel="stylesheet">
<style>
  :root{
    --navy:#0d3a52;
    --white:#ffffff;
    --hero-light:#f2f2f2;
    --hero-mid:#dcdcdc;
    --hero-dark:#b9b9b9;
  }
  *{box-sizing:border-box;margin:0;padding:0}
  html,body{width:1200px;height:840px;overflow:hidden;background:var(--white)}
  body{position:relative;font-family:"Roboto",sans-serif;color:var(--navy)}
  .hero{position:absolute;left:0;top:0;width:1200px;height:644px;
    background:
      radial-gradient(ellipse 420px 380px at 240px 430px, var(--hero-dark), transparent 70%),
      linear-gradient(115deg, var(--hero-mid) 0%, var(--hero-light) 45%, #e6e6e6 70%, var(--hero-light) 100%);}
  .brand{position:absolute;left:62px;top:30px;font-family:"Roboto Slab",serif;font-weight:700;
    font-size:48px;line-height:1;color:var(--navy);letter-spacing:.5px}
  .nav{position:absolute;top:39px;right:28px;display:flex;gap:0;list-style:none}
  .nav a{display:block;height:25px;line-height:25px;padding:0 8px;margin-left:6px;font-size:12.5px;
    color:var(--navy);text-decoration:none}
  .nav a.active{background:var(--navy);color:var(--white)}
  .headline{position:absolute;left:0;width:1200px;top:262px;text-align:center;font-family:"Roboto Slab",serif;
    font-weight:400;font-size:45px;line-height:59px;color:var(--navy)}
  .subline{position:absolute;left:0;width:1200px;top:397px;text-align:center;font-size:14.5px;color:var(--navy)}
  .service{position:absolute;top:610px;width:230px;text-align:center}
  .service .badge{display:block;margin:0 auto;width:82px;height:82px}
  .service h2{margin-top:22px;font-family:"Roboto Slab",serif;font-weight:400;font-size:18.5px;line-height:23px;color:var(--navy)}
  .footer{position:absolute;left:0;bottom:0;width:1200px;height:26px;background:var(--navy);color:var(--white);
    font-size:8.5px;line-height:26px;text-align:center}
</style>
</head>
<body>
  <div class="hero" role="img" aria-label="Foto: Bauleitung mit Schutzhelmen prüft Pläne vor einer modernen Glasfassade, entsättigt und aufgehellt"></div>

  <div class="brand">Brandvik</div>

  <ul class="nav">
    <li><a class="active" href="#">Startseite</a></li>
    <li><a href="#">Leistungen</a></li>
    <li><a href="#">Über uns</a></li>
    <li><a href="#">Referenzen</a></li>
    <li><a href="#">Kontakt</a></li>
  </ul>

  <h1 class="headline">Projektmanagement<br>und Projektsteuerung</h1>
  <p class="subline">von Bauvorhaben für Projektentwickler und Bauträger</p>

  <section class="service" style="left:242px">
    <svg class="badge" viewBox="0 0 82 82"><circle cx="41" cy="41" r="41" fill="#fff"/><circle cx="41" cy="41" r="30" fill="#0d3a52"/>
      <g fill="none" stroke="#fff" stroke-width="1.6" stroke-linecap="round"><rect x="28" y="28" width="10" height="10"/><path d="M33 30v6M30 33h6"/><circle cx="46" cy="32" r="5"/><path d="M43.5 32h5"/><path d="M23 52c6-4 10-4 16-2h8c2 0 2 3 0 3h-8M47 53l8-5c2-1 4 1 2 3l-10 6H30"/></g></svg>
    <h2>Betriebswirtschaftlichen Planung</h2>
  </section>

  <section class="service" style="left:479px">
    <svg class="badge" viewBox="0 0 82 82"><circle cx="41" cy="41" r="41" fill="#fff"/><circle cx="41" cy="41" r="30" fill="#0d3a52"/>
      <g fill="none" stroke="#fff" stroke-width="1.6" stroke-linecap="round"><rect x="27" y="24" width="26" height="34" rx="2"/><path d="M31 30h18M31 52h6M43 52h6"/><circle cx="39" cy="41" r="6"/><path d="M44 41h12"/></g></svg>
    <h2>Steuerung der baulichen Umsetzung</h2>
  </section>

  <section class="service" style="left:726px">
    <svg class="badge" viewBox="0 0 82 82"><circle cx="41" cy="41" r="41" fill="#fff"/><circle cx="41" cy="41" r="30" fill="#0d3a52"/>
      <g fill="none" stroke="#fff" stroke-width="1.6" stroke-linecap="round"><path d="M32 24h16l5 5v18M32 24v6"/><rect x="26" y="32" width="20" height="24"/><path d="M30 37h12M30 41h8"/><circle cx="41" cy="48" r="4"/><path d="M48 48h8M48 52h8M48 56h8"/></g></svg>
    <h2>Steuerung Marketing und Vertriebsaktivitäten</h2>
  </section>

  <footer class="footer">© 2017 Brandvik Real Estate GmbH</footer>
</body>
</html>
```